Business Cards for Communications Technology Company

We are an innovative software company based in Tropical North Queensland, Australia. We have several brands with a focus on communications software for businesses. We are looking for a business card that is very innovate and creative whilst still remaining professional on a corporate level.

Our internal culture is very progressive and expresses a blend between the clarity of our natural surroundings and the highly technological industry we work in. Our current branding blends a modern minimalist typeface with the desire to push the boundaries in the way we communicate.

This is a corporate level business card for the communications software industry and may possibly also encompass our brands MarNetwork, PelFax, TukMailer and our B2B marketing service—with our companies name being Viresca Partners. Showing other brands on the business card is optional not compulsory.

Technical notes:

-We will attach all logo's and some examples of our corporate branding
- Would be willing to print with various papers, embossed, metallic ink, curved edges etc. in a standard business card size

Sample content:

Rowan Pellick
Senior Account Manager
Phone: 1300 842 916 / +617 4583 2764
Email: r.pellick@viresca.com.au
Web: www.viresca.com.au

Sincerely,
Viresca Partners.

```html
<!DOCTYPE html>
<html lang="en">
<head>
<meta charset="utf-8">
<title>Viresca Partners – Business Cards</title>
<link href="https://fonts.googleapis.com/css2?family=Questrial&family=Lato:wght@400;700&display=swap" rel="stylesheet">
<style>
  :root {
    --backdrop: #e4e1db;
    --ink-black: #0d0d0d;
    --ink-dark: #2b2b2b;
    --silver: #c2c4c6;
    --silver-dark: #8d9093;
    --leaf: #8cc63f;
    --leaf-deep: #6aa72e;
    --paper: #ffffff;
    --paper-grey: #e9eaeb;
    --brand-orange: #f07a22;
    --brand-green: #7cbf3a;
    --brand-blue: #3f6fc0;
  }
  * { box-sizing: border-box; margin: 0; padding: 0; }
  html, body { width: 900px; height: 1200px; overflow: hidden; }
  body { background: var(--backdrop); position: relative; font-family: "Lato", sans-serif; }

  .card {
    position: absolute;
    border-radius: 24px;
    overflow: hidden;
    box-shadow: 0 6px 14px rgba(0,0,0,.25);
  }
  .card__shapes { position: absolute; inset: 0; width: 100%; height: 100%; }

  /* Front */
  .card--front { left: 85px; top: 133px; width: 735px; height: 430px; background: var(--paper-grey); }
  .front__name {
    position: absolute; left: 0; right: 0; top: 108px;
    text-align: center;
    font-family: "Questrial", sans-serif;
    font-size: 56px; letter-spacing: 1px;
    color: var(--silver);
  }
  .front__brands {
    position: absolute; left: 40px; right: 40px; top: 352px;
    display: flex; justify-content: space-between; align-items: center;
  }
  .brand {
    display: flex; align-items: center; gap: 8px;
    font-family: "Lato", sans-serif; font-weight: 700; font-size: 30px;
  }
  .brand__dot { width: 14px; height: 14px; border-radius: 50%; }
  .brand--network { color: var(--brand-orange); }
  .brand--network .brand__dot { background: var(--brand-orange); }
  .brand--fax { color: var(--brand-green); }
  .brand--fax .brand__dot { background: var(--brand-green); }
  .brand--mailer { color: var(--brand-blue); }
  .brand--mailer .brand__dot { background: var(--brand-blue); }

  /* Back */
  .card--back { left: 88px; top: 636px; width: 732px; height: 414px; background: var(--paper); }
  .back__content { position: absolute; left: 0; right: 0; top: 88px; text-align: center; }
  .back__company {
    font-family: "Questrial", sans-serif; font-size: 60px;
    color: var(--ink-dark); letter-spacing: 1px; line-height: 1;
  }
  .back__person {
    margin-top: 38px;
    font-family: "Questrial", sans-serif; font-size: 21px;
    color: var(--ink-dark); letter-spacing: .5px; line-height: 1;
  }
  .back__role {
    margin-top: 6px;
    font-family: "Questrial", sans-serif; font-size: 16px;
    color: var(--leaf-deep);
  }
  .back__rule { width: 76px; height: 4px; background: var(--ink-dark); margin: 18px auto 16px; }
  .back__contact { font-size: 17px; color: var(--ink-dark); line-height: 26px; }
</style>
</head>
<body>

  <section class="card card--front" aria-label="Card front">
    <svg class="card__shapes" viewBox="0 0 735 430" preserveAspectRatio="none" aria-hidden="true">
      <defs>
        <linearGradient id="leafBand" x1="0" y1="0" x2="1" y2="0">
          <stop offset="0" stop-color="#6aa72e"/>
          <stop offset="1" stop-color="#9bd14a"/>
        </linearGradient>
      </defs>
      <path d="M0,0 H735 V185 C560,280 300,322 0,330 Z" fill="url(#leafBand)"/>
      <path d="M0,0 H735 V160 C560,262 300,302 0,308 Z" fill="var(--ink-black)"/>
    </svg>
    <div class="front__name">Viresca Partners</div>
    <div class="front__brands">
      <span class="brand brand--network">MarNetwork<span class="brand__dot"></span></span>
      <span class="brand brand--fax">PelFax<span class="brand__dot"></span></span>
      <span class="brand brand--mailer">TukMailer<span class="brand__dot"></span></span>
    </div>
  </section>

  <section class="card card--back" aria-label="Card back">
    <svg class="card__shapes" viewBox="0 0 732 414" preserveAspectRatio="none" aria-hidden="true">
      <defs>
        <linearGradient id="leafFill" x1="0" y1="0" x2="1" y2="1">
          <stop offset="0" stop-color="#9bd14a"/>
          <stop offset="1" stop-color="#6aa72e"/>
        </linearGradient>
        <linearGradient id="silverStrip" x1="0" y1="0" x2="1" y2="0">
          <stop offset="0" stop-color="#e6e7e8"/>
          <stop offset=".5" stop-color="#9a9da0"/>
          <stop offset="1" stop-color="#d8d9da"/>
        </linearGradient>
      </defs>
      <!-- top right corner -->
      <path d="M340,0 H732 V200 C640,90 500,20 340,0 Z" fill="url(#silverStrip)"/>
      <path d="M420,0 H732 V175 C650,80 540,18 420,0 Z" fill="url(#leafFill)"/>
      <!-- bottom left corner -->
      <path d="M0,230 C90,330 250,395 470,414 H0 Z" fill="url(#silverStrip)"/>
      <path d="M0,262 C100,345 240,395 400,414 H0 Z" fill="url(#leafFill)"/>
    </svg>
    <div class="back__content">
      <div class="back__company">Viresca Partners</div>
      <div class="back__person">ROWAN PELLICK</div>
      <div class="back__role">Senior Account Manager</div>
      <div class="back__rule"></div>
      <div class="back__contact">
        <div>1300 842 916 | +617 4583 2764</div>
        <div>r.pellick@viresca.com.au | www.viresca.com.au</div>
      </div>
    </div>
  </section>

</body>
</html>
```